Print & Packaging Design for Wee Fern Teething & Healing Necklaces

Bring your Creative Juices this-a way! Smart, savvy, up-market business needs a logo & swing tags! Do you have what it takes?

```html
<!DOCTYPE html>
<html lang="en">
<head>
<meta charset="utf-8">
<title>Wee Fern Teething &amp; Healing Necklaces – Swing Tags</title>
<link href="https://fonts.googleapis.com/css2?family=Fredoka:wght@600&family=Source+Sans+3:wght@600&display=swap" rel="stylesheet">
<style>
  :root {
    --backdrop: #f1f1f1;
    --tag-peach: #f4c9ae;
    --tag-peach-light: #f8dccb;
    --accent-pink: #e6127f;
    --daisy-coral: #f29a86;
    --brand-blue: #2a6fb8;
    --ink: #1d1d1d;
    --body-ink: #2e2a28;
    --eyelet-ring: #d9d9d9;
    --eyelet-hole: #111111;
    --photo-light: #fbf4ef;
    --photo-warm: #e9c0a4;
  }
  html, body {
    margin: 0;
    width: 1200px;
    height: 800px;
    overflow: hidden;
    background: var(--backdrop);
  }
  .canvas {
    position: relative;
    width: 1200px;
    height: 800px;
  }
  .swing-tag {
    position: absolute;
    background: var(--tag-peach);
    border-radius: 22px;
    overflow: hidden;
  }
  .swing-tag--front { left: 160px; top: 50px; width: 860px; height: 350px; }
  .swing-tag--back  { left: 190px; top: 425px; width: 820px; height: 320px; }
  .tag-shapes {
    position: absolute;
    inset: 0;
    width: 100%;
    height: 100%;
  }
  .eyelet {
    position: absolute;
    width: 38px;
    height: 38px;
    border-radius: 50%;
    background: var(--eyelet-hole);
    border: 6px solid var(--eyelet-ring);
  }
  .swing-tag--front .eyelet { left: 28px; top: 158px; }
  .swing-tag--back .eyelet  { left: 26px; top: 138px; }
  .daisy {
    position: absolute;
    border-radius: 50%;
    background: var(--tag-peach-light);
    opacity: .75;
  }
  .daisy--accent { background: var(--daisy-coral); opacity: .9; }
  .brand {
    position: absolute;
    text-align: center;
  }
  .swing-tag--front .brand { left: 480px; top: 105px; width: 360px; }
  .swing-tag--back .brand  { left: 545px; top: 95px; width: 260px; }
  .brand-name {
    font-family: "Fredoka", sans-serif;
    font-weight: 600;
    color: var(--brand-blue);
    line-height: 1;
    margin: 0;
  }
  .swing-tag--front .brand-name { font-size: 70px; }
  .swing-tag--back .brand-name  { font-size: 50px; }
  .brand-tagline {
    font-family: "Fredoka", sans-serif;
    font-weight: 600;
    color: var(--ink);
    line-height: 1.2;
    margin: 14px 0 0;
    white-space: nowrap;
  }
  .swing-tag--front .brand-tagline { font-size: 22px; }
  .swing-tag--back .brand-tagline  { font-size: 15px; margin-top: 12px; }
  .benefits {
    position: absolute;
    left: 90px;
    top: 22px;
    width: 360px;
    margin: 0;
    padding: 0;
    list-style: none;
    font-family: "Source Sans 3", sans-serif;
    font-weight: 600;
    font-size: 21px;
    line-height: 30px;
    color: var(--body-ink);
  }
  .benefits li {
    padding-left: 15px;
    text-indent: -15px;
  }
  .benefits li::before { content: "- "; }
</style>
</head>
<body>
<main class="canvas">

  <section class="swing-tag swing-tag--front" aria-label="Swing tag front">
    <svg class="tag-shapes" viewBox="0 0 860 350" preserveAspectRatio="none">
      <defs>
        <linearGradient id="photoTone" x1="0" y1="0" x2="1" y2="1">
          <stop offset="0" stop-color="var(--photo-light)"/>
          <stop offset="1" stop-color="var(--photo-warm)"/>
        </linearGradient>
      </defs>
      <polygon points="0,0 400,0 372,350 0,350" fill="url(#photoTone)" role="img" aria-label="Photo of a mother kissing her smiling baby"/>
      <polygon points="400,0 436,0 408,350 372,350" fill="var(--accent-pink)"/>
    </svg>
    <span class="eyelet"></span>
    <span class="daisy" role="img" aria-label="Daisy flower" style="left:700px;top:10px;width:40px;height:40px;"></span>
    <span class="daisy daisy--accent" role="img" aria-label="Daisy flower" style="left:380px;top:240px;width:120px;height:120px;"></span>
    <span class="daisy" role="img" aria-label="Daisy flower" style="left:720px;top:220px;width:110px;height:110px;"></span>
    <div class="brand">
      <p class="brand-name">Wee Fern</p>
      <p class="brand-tagline">Teething &amp; Healing Necklaces</p>
    </div>
  </section>

  <section class="swing-tag swing-tag--back" aria-label="Swing tag back">
    <svg class="tag-shapes" viewBox="0 0 820 320" preserveAspectRatio="none">
      <polygon points="497,0 540,0 520,320 477,320" fill="var(--accent-pink)"/>
    </svg>
    <span class="eyelet"></span>
    <span class="daisy" role="img" aria-label="Daisy flower" style="left:680px;top:14px;width:40px;height:40px;"></span>
    <span class="daisy daisy--accent" role="img" aria-label="Daisy flower" style="left:460px;top:210px;width:120px;height:120px;"></span>
    <span class="daisy" role="img" aria-label="Daisy flower" style="left:690px;top:225px;width:100px;height:100px;"></span>
    <ul class="benefits">
      <li>natural pain relief for your babe.</li>
      <li>relieve your babes pain and sleep better at night.</li>
      <li>sleep better at night knowing you've helped to ease your babes pain.</li>
      <li>baltic amber teething necklaces.</li>
      <li>gemstone nursing necklaces.</li>
      <li>fertility and birthing jewellery.</li>
      <li>natural healing jewellery.</li>
    </ul>
    <div class="brand">
      <p class="brand-name">Wee Fern</p>
      <p class="brand-tagline">Teething &amp; Healing Necklaces</p>
    </div>
  </section>

</main>
</body>
</html>
```